Roof wash and Gutter Cleaning

Would like to see our colors and logo incorporated into design along with phone number and before/after picture(s). We use a non pressure softwash process we use unlike high pressure. We are a exterior cleaning company that likes to set our standards high with safe methods to cleaning the everyday surfaces on homes.
“Serving the Tri-State Area”
A list of our services:
House washing
Shingle and metal roof washing
Deck cleaning
Window cleaning
Concrete cleaning
Gutter cleaning
514-362-0917
We do not need the address section as these will be more for our meet and greets. As well handed out as clipped door  postcards.

Shingle roof wash and gutter cleaning

```html
<!DOCTYPE html>
<html lang="en">
<head>
<meta charset="utf-8">
<title>Brightwell Exterior Cleaning – Postcard</title>
<link href="https://fonts.googleapis.com/css2?family=Roboto:ital,wght@0,300;0,400;0,500;0,700;1,400&display=swap" rel="stylesheet">
<style>
  :root{
    --stage:#6aaad9;
    --card:#ffffff;
    --brand-blue:#2d5fa8;
    --tagline-grey:#8c8c8c;
    --service-blue:#6aaee0;
    --service-grey:#3a3a3a;
    --wash:#dde9f5;
    --frame:#f1f2f4;
    --frame-shadow:rgba(0,0,0,.18);
    --caption:#555;
    --phone-green:#5cb84a;
  }
  *{box-sizing:border-box;margin:0;padding:0}
  html,body{width:1200px;height:1120px;overflow:hidden}
  body{background:var(--stage);font-family:"Roboto",Arial,sans-serif;position:relative}

  .size-label{position:absolute;left:111px;top:78px;font-size:11px;font-style:italic;letter-spacing:2px;color:#2e4b6a}

  .card{position:absolute;left:112px;width:973px;height:433px;background:var(--card);overflow:hidden}
  .card--front{top:101px}
  .card--back{top:587px}

  .wash{position:absolute;inset:0;width:100%;height:100%}

  .brand-word{position:absolute;color:var(--brand-blue);font-weight:500;line-height:1;text-align:center;white-space:nowrap}
  .brand-tagline{position:absolute;color:var(--tagline-grey);font-weight:400;font-style:italic;line-height:1;text-align:center;white-space:nowrap}
  .card--front .brand-word{left:94px;top:178px;width:340px;font-size:72px;letter-spacing:1px}
  .card--front .brand-tagline{left:64px;top:312px;width:400px;font-size:20px}
  .card--back .brand-word{left:29px;top:312px;width:200px;font-size:42px}
  .card--back .brand-tagline{left:19px;top:395px;width:220px;font-size:11px}

  .phone{position:absolute;display:flex;align-items:center;color:var(--brand-blue);font-weight:500;line-height:1;white-space:nowrap}
  .phone svg{flex:none}
  .card--front .phone{left:76px;top:350px;font-size:38px;letter-spacing:5px;gap:10px}
  .card--back .phone{left:231px;top:384px;font-size:26px;letter-spacing:3.5px;gap:8px}

  .services{position:absolute;inset:0}
  .service{position:absolute;display:flex;align-items:baseline;gap:5px;line-height:1;white-space:nowrap}
  .lead{font-weight:300;font-size:27px;color:var(--service-grey)}
  .main{font-weight:500;font-size:47px;color:var(--service-blue);letter-spacing:-.3px}

  .snap{position:absolute;background:var(--frame);padding:10px 10px 0;box-shadow:0 2px 6px var(--frame-shadow)}
  .snap .photo{width:100%}
  .snap .caption{display:block;text-align:right;font-size:11px;font-style:italic;letter-spacing:1.5px;color:var(--caption);padding:6px 2px 6px;line-height:1}
  .snap--left-caption .caption{text-align:left}
  .snap--tucked .caption{padding-right:26px}
</style>
</head>
<body>

<p class="size-label">size - 9x4 inch</p>

<!-- FRONT -->
<section class="card card--front">
  <svg class="wash" viewBox="0 0 973 433" aria-hidden="true">
    <path fill="var(--wash)" d="M160 433 C175 370 240 330 320 318 C420 300 470 250 560 228 C640 210 700 240 760 210 C820 182 850 150 900 150 C950 150 973 175 973 200 L973 433 Z"/>
    <path fill="var(--card)" d="M560 433 C600 380 680 360 760 370 C830 380 880 330 940 320 L973 318 L973 433 Z" opacity=".9"/>
    <circle cx="846" cy="118" r="10" fill="var(--wash)"/>
    <circle cx="900" cy="150" r="15" fill="var(--wash)"/>
    <circle cx="925" cy="122" r="7" fill="var(--wash)"/>
    <circle cx="932" cy="398" r="14" fill="var(--wash)"/>
  </svg>

  <p class="brand-word">Brightwell</p>
  <p class="brand-tagline">Exterior Cleaning &amp; Maintenance Co.</p>

  <div class="phone">
    <svg width="30" height="30" viewBox="0 0 30 30" aria-hidden="true">
      <circle cx="15" cy="15" r="14" fill="var(--phone-green)" stroke="var(--brand-blue)" stroke-width="2"/>
      <path fill="var(--brand-blue)" d="M10.5 8.5c.8-.6 1.6-.4 2 .3l1.3 2.4c.3.6.2 1.2-.3 1.6l-.9.7c.6 1.5 1.8 2.8 3.3 3.6l.8-.9c.4-.5 1.1-.6 1.6-.3l2.4 1.3c.7.4.9 1.3.3 2l-1 1.2c-.7.8-1.9 1-2.9.6-3.6-1.5-6.3-4.3-7.7-7.9-.4-1 0-2.2.8-2.8z"/>
    </svg>
    <span>514-362-0917</span>
  </div>

  <div class="services">
    <div class="service" style="left:638px;top:58px"><span class="lead">house</span></div>
    <div class="service" style="left:638px;top:71px"><span class="main">washing</span></div>
    <div class="service" style="left:572px;top:109px"><span class="lead">shingle and metal</span></div>
    <div class="service" style="left:573px;top:128px"><span class="main">roof washing</span></div>
    <div class="service" style="left:638px;top:167px"><span class="lead">deck</span><span class="main">cleaning</span></div>
    <div class="service" style="left:524px;top:209px"><span class="lead">window</span><span class="main">cleaning</span></div>
    <div class="service" style="left:598px;top:249px"><span class="lead">concrete</span><span class="main">cleaning</span></div>
    <div class="service" style="left:562px;top:282px"><span class="lead">gutter</span><span class="main">cleaning</span></div>
  </div>
</section>

<!-- BACK -->
<section class="card card--back">
  <svg class="wash" viewBox="0 0 973 433" aria-hidden="true">
    <path fill="var(--wash)" d="M180 433 C200 370 250 330 330 320 C430 305 500 250 600 245 C700 240 760 200 830 200 C900 200 940 170 973 160 L973 433 Z"/>
    <path fill="var(--card)" d="M620 433 C660 390 730 370 800 375 C870 380 920 340 973 330 L973 433 Z" opacity=".9"/>
    <circle cx="868" cy="330" r="8" fill="var(--wash)"/>
    <circle cx="932" cy="395" r="13" fill="var(--wash)"/>
  </svg>

  <figure class="snap snap--left-caption" style="left:44px;top:51px;width:191px;transform:rotate(-2deg)">
    <div class="photo" role="img" aria-label="House with dormers and front porch before washing" style="height:132px;background:linear-gradient(180deg,#b9c6d3 0%,#8f8a7e 45%,#6b5a47 70%,#5d6a3e 100%)"></div>
    <figcaption class="caption">before</figcaption>
  </figure>

  <figure class="snap snap--left-caption" style="left:190px;top:92px;width:193px;transform:rotate(-1.5deg)">
    <div class="photo" role="img" aria-label="Same house after a soft wash, bright siding and clean roof" style="height:132px;background:linear-gradient(180deg,#c8d2dc 0%,#9a9286 45%,#7a624a 68%,#5f6b3c 100%)"></div>
    <figcaption class="caption">after</figcaption>
  </figure>

  <figure class="snap" style="left:351px;top:150px;width:196px;transform:rotate(-2deg)">
    <div class="photo" role="img" aria-label="Shingle roof after washing with vent pipe and trees" style="height:130px;background:linear-gradient(180deg,#9e968c 0%,#9c9a95 35%,#b6b3ae 100%)"></div>
    <figcaption class="caption">after</figcaption>
  </figure>

  <figure class="snap snap--tucked" style="left:486px;top:62px;width:195px;transform:rotate(2deg)">
    <div class="photo" role="img" aria-label="Stained shingle roof before washing" style="height:128px;background:linear-gradient(180deg,#8d8276 0%,#6c6660 40%,#7b756d 100%)"></div>
    <figcaption class="caption">before</figcaption>
  </figure>

  <figure class="snap" style="left:661px;top:148px;width:146px;transform:rotate(-3deg)">
    <div class="photo" role="img" aria-label="Gutter clogged with leaves before cleaning" style="height:164px;background:linear-gradient(180deg,#b8c0c4 0%,#8a7a68 40%,#6e5236 100%)"></div>
    <figcaption class="caption">before</figcaption>
  </figure>

  <figure class="snap" style="left:780px;top:62px;width:155px;transform:rotate(2deg)">
    <div class="photo" role="img" aria-label="Clean gutter along a shingle roof after cleaning" style="height:166px;background:linear-gradient(90deg,#8a5a44 0%,#9e6a52 50%,#a89a8c 100%)"></div>
    <figcaption class="caption">after</figcaption>
  </figure>

  <p class="brand-word">Brightwell</p>
  <p class="brand-tagline">Exterior Cleaning &amp; Maintenance Co.</p>

  <div class="phone">
    <svg width="21" height="21" viewBox="0 0 30 30" aria-hidden="true">
      <circle cx="15" cy="15" r="14" fill="var(--phone-green)" stroke="var(--brand-blue)" stroke-width="2"/>
      <path fill="var(--brand-blue)" d="M10.5 8.5c.8-.6 1.6-.4 2 .3l1.3 2.4c.3.6.2 1.2-.3 1.6l-.9.7c.6 1.5 1.8 2.8 3.3 3.6l.8-.9c.4-.5 1.1-.6 1.6-.3l2.4 1.3c.7.4.9 1.3.3 2l-1 1.2c-.7.8-1.9 1-2.9.6-3.6-1.5-6.3-4.3-7.7-7.9-.4-1 0-2.2.8-2.8z"/>
    </svg>
    <span>514-362-0917</span>
  </div>
</section>

</body>
</html>
```